Your Harbor Agent Website Design

Creative Brief: Website Design for Your Harbor Agent
- Project Overview: Design a website for our new brand, "Your Harbor Agent". Your Harbor Agent is a service that matches clients with the perfect realtor. The primary function of this site is to serve as a lead generation hub, to generate leads of people who are looking to either buy or sell their house and need a great realtor. The site needs to have a very clean, modern design using sites like Tallyquest, Brickwell, Lantern, and Vexomill as an example. The site also needs to have a primary lead capture capability through a multi-step form or questionnaire that indicates if they are buying or selling, and depending on that selection, creates two different flows.

Target Audience:
- Homebuyers and sellers in the Denver area
- Individuals looking for high-quality realtor services
- Users seeking a seamless and professional online & home buying/selling experience

Objectives:
- Create a visually appealing, modern website with a strong emphasis on lead generation.
- Design advanced, multi-step forms for efficient lead capture.
- Ensure the website is user-friendly and optimized for both desktop and mobile devices.

Pages to Design:
Home Page:
- Engaging hero section with a clear call to action and the ability to enter the form flow
- Brief introduction to Your Harbor Agent and its unique value proposition
- Key features & benefits of being matched with a realtor by Your Harbor Agent
- Testimonials and success stories
- Lead capture form

About Page:
- Overview of Your Harbor Agent’s mission and values
- Professional and trust-building imagery

How it Works Page:
- Step-by-step explanation of the matching process (complete the form and we will match you with a realtor)
- Visual aids (icons, graphics) to simplify complex information
- Customer journey map from inquiry to successful match & sale of home
- Lead capture form

Contact Us Page:
- Simple and accessible contact form
- Contact details
- Call to action for immediate inquiries

Blog Template:
- Clean, easy-to-read layout for blog posts, primarily location/neighborhood guides as well as standard blogs
- Sidebar for recent posts, categories, and tags
- Social sharing buttons
- Lead capture form embedded within blog posts

Design Style:
- Modern and professional with a focus on usability
- Clean lines and intuitive navigation
- Use of curved corners and minimal straight lines for a sleek look
- Incorporation of graphic design elements, potentially including 3D and isomorphic design
- Inspired by sites like Tallyquest, Brickwell, Lantern, and Vexomill
Consistent color scheme and typography

Visual References:
- Tallyquest: For its professional and corporate look
- Brickwell and Lantern: For their user-friendly interfaces and modern design
- Vexomill: For its clean and functional layout

Target Market(s)

- Homebuyers and sellers in the Denver area, Individuals looking for high-quality realtor services, Users seeking a seamless and professional home buying/selling experience

Industry/Entity Type

Real Estate

Number of Pages Required

5+ page

Requirements
Must have
• Fully designed website with lead capture functionality based on brief
Nice to have
• Designed in Figma, Starting / Placeholder copy

```html
<!DOCTYPE html>
<html lang="en">
<head>
<meta charset="utf-8">
<title>HarborMatch – Find Your Real Estate Agent</title>
<link href="https://fonts.googleapis.com/css2?family=Lexend:wght@300;400;500;600;700&display=swap" rel="stylesheet">
<style>
:root{
  --navy:#12284f;
  --blue:#1a73d9;
  --sky:#2b9cf0;
  --light:#eaf3fc;
  --mist:#d6e6f6;
  --orange:#fb9b0b;
  --text:#2b3445;
  --muted:#6b7689;
  --line:#dfe6ef;
  --white:#fff;
}
*{box-sizing:border-box;margin:0;padding:0}
html,body{width:1200px;height:4637px;overflow:hidden}
body{position:relative;font-family:"Lexend",sans-serif;color:var(--text);background:var(--white)}
.abs{position:absolute}
.fill{position:absolute}
.brand{font-size:30px;font-weight:400;color:var(--navy);letter-spacing:-.5px;white-space:nowrap}
/* nav */
.nav{position:absolute;top:24px;left:0;width:1200px;height:40px}
.nav .brand{position:absolute;left:94px;top:0}
.nav ul{position:absolute;left:366px;top:12px;display:flex;list-style:none;font-size:13px;color:var(--navy);white-space:nowrap}
.nav li{padding:0 21px;border-left:1px solid #9fb4d0;line-height:16px}
.nav li:first-child{border-left:none}
.btn{display:inline-flex;align-items:center;justify-content:center;border-radius:30px;font-weight:500;color:#fff;white-space:nowrap}
.btn-blue{position:absolute;left:965px;top:1px;background:linear-gradient(90deg,var(--blue),var(--sky));height:38px;width:136px;font-size:13px}
.btn-orange{background:var(--orange);font-size:14px;font-weight:600}
/* headings */
.h-light{color:var(--sky);font-weight:300}
.h-bold{color:var(--navy);font-weight:700}
/* hero */
.hero-title{left:97px;top:162px;font-size:37px;line-height:44px}
.hero-sub{left:97px;top:264px;width:470px;font-size:13px;line-height:19px;color:#333}
.agent-card{left:94px;top:352px;width:486px;height:178px;border:1px solid var(--line);border-radius:4px;background:#fff;box-shadow:0 4px 18px rgba(20,60,120,.08)}
.agent-tab{left:94px;top:325px;width:196px;height:36px;border:1px solid var(--line);border-bottom:none;border-radius:4px 4px 0 0;background:#fff;font-size:14px;font-weight:500;color:var(--navy);padding:9px 0 0 24px}
.agent-card p{position:absolute;left:34px;top:48px;width:410px;font-size:11px;line-height:16px;color:var(--muted)}
.email-row{position:absolute;left:34px;top:104px;width:420px;height:40px;display:flex}
.email-row span{flex:1;background:#f1f3f6;border:1px solid var(--line);font-size:11px;color:#555;padding:12px 0 0 20px}
.email-row b{width:148px;background:var(--orange);color:#fff;font-size:14px;font-weight:600;display:flex;align-items:center;justify-content:center}
/* about */
.ring{border-radius:50%;border:2px solid var(--mist)}
.badge{background:#fff;border-radius:6px;text-align:center;box-shadow:0 4px 14px rgba(0,0,0,.08)}
.badge strong{display:block;color:var(--blue);font-size:22px;font-weight:700}
.badge span{font-size:13px;color:var(--navy);line-height:16px;display:block}
.about-title{left:605px;top:780px;font-size:40px;line-height:49px}
.about-rule{left:605px;top:880px;width:72px;height:4px;background:var(--blue)}
.about-text{left:608px;width:485px;font-size:15px;line-height:23px;color:#444}
/* steps */
.step{top:1236px;width:300px;height:224px;border:1px solid var(--line);border-radius:6px;background:#fff;text-align:center;padding-top:20px}
.step h3{font-size:14px;font-weight:600;color:var(--navy);margin-top:18px}
.step p{font-size:11px;line-height:16px;color:var(--muted);margin:12px auto 0;width:230px}
.step.active{background:linear-gradient(135deg,#1a5fd0,#3aa3ee);border:none}
.step.active h3,.step.active p{color:#fff}
.dot-blue{border-radius:50%;background:radial-gradient(circle at 40% 40%,#3aa7f5,#1473e0)}
/* why */
.sec-title{left:0;width:1200px;text-align:center;font-size:40px}
.feat{width:270px}
.feat h4{font-size:16px;font-weight:600;color:var(--navy);white-space:nowrap}
.feat p{font-size:12px;line-height:16px;color:var(--muted);margin-top:4px;white-space:nowrap}
.feat.right-al{text-align:right}
.icon-c{width:72px;height:72px;border-radius:50%;display:flex;align-items:center;justify-content:center}
.icon-c.b{background:var(--sky)}
.icon-c.n{background:var(--navy)}
/* testimonials */
.tcard{top:2592px;width:318px;height:264px;background:#fff;border:1px solid var(--line);border-radius:6px;box-shadow:0 4px 18px rgba(20,60,120,.06)}
.tcard .q{position:absolute;left:30px;top:18px;font-size:60px;line-height:60px;color:#b9d3ef;font-weight:700}
.tcard p{position:absolute;left:30px;top:70px;width:262px;font-size:11px;line-height:20px;font-style:italic;color:#444}
.tcard .who{position:absolute;left:24px;top:196px;display:flex;align-items:center;gap:12px;font-size:11px;font-weight:600;color:var(--navy)}
.avatar{width:34px;height:34px;border-radius:50%;background:linear-gradient(135deg,#c59a7a,#6e5546)}
.stars{color:var(--orange);font-size:14px;letter-spacing:5px;display:block;margin-top:4px}
.rev{position:absolute;right:26px;top:206px;width:22px;height:22px;border-radius:50%;border:3px solid #e44b3c}
/* story */
.story{left:195px;top:3060px;width:895px;height:485px;border-radius:26px;background:linear-gradient(120deg,#1559d4,#2b8ce8 60%,#3aa6ef)}
.story h2{position:absolute;left:317px;top:90px;font-size:38px;font-weight:300;color:#fff}
.story h2 b{font-weight:700}
.story p{position:absolute;left:317px;top:150px;width:540px;font-size:19px;line-height:31px;font-style:italic;font-weight:300;color:#fff}
.story .name{position:absolute;left:317px;top:340px;font-size:18px;font-weight:500;color:#fff}
/* form */
.form-card{left:172px;top:3910px;width:840px;height:430px;background:#fff;border-radius:6px;box-shadow:0 6px 24px rgba(20,60,120,.10)}
.field{position:absolute;height:44px;background:#f6f8fb;border:1px solid var(--line);border-radius:3px;font-size:12px;color:#444;padding:14px 0 0 18px}
.field svg{position:absolute;right:16px;top:17px}
/* footer */
.footer-col h5{font-size:17px;font-weight:500;color:var(--navy);border-left:2px solid var(--blue);padding-left:8px}
.footer-col li{list-style:none;font-size:13px;color:#444;margin-top:12px;padding-left:14px}
.vline{width:1px;background:var(--line);top:4385px;height:140px}
.soc{width:36px;height:36px;border-radius:50%;background:var(--blue)}
</style>
</head>
<body>

<!-- NAV -->
<header class="nav">
  <div class="brand">HarborMatch</div>
  <ul>
    <li>About Us</li><li>How it works</li><li>Benefits &amp; Features</li><li>Contact Us</li>
  </ul>
  <span class="btn btn-blue">Get Started</span>
</header>

<!-- HERO -->
<div class="fill" role="img" aria-label="Soft pale blue city skyline fading into a light green park" style="left:0;top:420px;width:1200px;height:290px;background:linear-gradient(180deg,#fff 0%,#e6f0fa 35%,#dceaf7 65%,#eef5e2 88%,#fff 100%)"></div>
<h1 class="abs hero-title"><span class="h-light">Connect with the Perfect</span><br><span class="h-bold">Real Estate Agent – Fast</span></h1>
<svg class="abs" style="left:560px;top:215px" width="90" height="50"><path d="M2 14 Q30 50 82 38" fill="none" stroke="#2b9cf0" stroke-width="1.5" stroke-dasharray="4 4"/><path d="M76 33 L84 38 L76 43" fill="none" stroke="#2b9cf0" stroke-width="1.5"/></svg>
<p class="abs hero-sub">Experience personalized service, unmatched expertise, and rapid connections with top agents tailored to your unique needs.</p>
<div class="abs agent-card">
  <p>Lorem ipsum dolor sit amet, consectetur adipiscing elit, sed do eiusmod tempor incididunt ut labore et dolore.</p>
  <div class="email-row"><span>Email address</span><b>Next Step</b></div>
</div>
<div class="abs agent-tab">Find My Agent Now</div>
<div class="abs ring" style="left:630px;top:115px;width:500px;height:500px;border-color:#cfe2f5"></div>
<div class="abs" role="img" aria-label="Isometric suburban house on a green lawn against a blue city skyline" style="left:640px;top:125px;width:480px;height:420px;border-radius:240px 240px 40px 40px;background:linear-gradient(180deg,#3d9ff0 0%,#5bb4f3 55%,#8fcf6a 80%,#e9eef2 100%)"></div>

<!-- ABOUT -->
<div class="abs ring" style="left:85px;top:705px;width:440px;height:480px;border-radius:50%"></div>
<div class="abs" role="img" aria-label="Smiling real estate agent in a grey blazer holding a tablet" style="left:112px;top:740px;width:405px;height:425px;border-radius:50%;background:radial-gradient(circle at 50% 45%,#dfe6ec,#aeb9c4 70%,#8b96a3)"></div>
<div class="abs badge" style="left:80px;top:885px;width:135px;height:80px;padding-top:8px"><strong>100%</strong><span>CLIENT<br>SATISFACTION</span></div>
<div class="abs badge" style="left:345px;top:1000px;width:140px;height:80px;padding-top:14px"><strong>1,000’s</strong><span>OF AGENTS</span></div>
<h2 class="abs about-title"><span class="h-light">Your Trusted Partner in</span><br><span class="h-bold">Real Estate Success</span></h2>
<div class="abs about-rule"></div>
<p class="abs about-text" style="top:912px">At HarborMatch, we believe that the right real estate agent can make all the difference in your home buying or selling experience. With our advanced matching technology, we connect you with agents who not only know the market but understand your unique needs.</p>
<p class="abs about-text" style="top:1052px">We are dedicated to making every transaction smooth and successful. Trust HarborMatch to guide you through every step of your real estate journey.</p>

<!-- STEPS -->
<div class="fill" role="img" aria-label="Faint pale blue buildings and trees along the bottom of the section" style="left:0;top:1240px;width:1200px;height:360px;background:linear-gradient(180deg,rgba(255,255,255,0) 0%,#e8eff8 55%,#dde8f4 85%,#fff 100%)"></div>
<div class="abs dot-blue" style="left:1017px;top:1210px;width:76px;height:76px"></div>
<div class="abs dot-blue" style="left:122px;top:1420px;width:52px;height:52px"></div>
<div class="abs step" style="left:130px">
  <svg width="66" height="58" viewBox="0 0 66 58" fill="none" stroke="#1a73d9" stroke-width="2.5"><circle cx="30" cy="26" r="20"/><path d="M44 40 L60 55"/><path d="M20 28 L30 19 L40 28 M23 26 V36 H37 V26"/></svg>
  <h3>FIND YOUR MATCH</h3>
  <p>Use our quick search to connect with top local agents who fit your needs.</p>
</div>
<div class="abs step active" style="left:448px">
  <svg width="66" height="58" viewBox="0 0 66 58" fill="none" stroke="#fff" stroke-width="2.5"><path d="M8 30 L33 8 L58 30"/><path d="M14 26 V52 H52 V26"/><path d="M20 40 L30 34 L36 38 L46 34"/></svg>
  <h3>GET CONNECTED</h3>
  <p>We’ll introduce you to your matched agent to start the process immediately.</p>
</div>
<div class="abs step" style="left:766px">
  <svg width="66" height="58" viewBox="0 0 66 58" fill="none" stroke="#1a73d9" stroke-width="2.5"><rect x="24" y="4" width="30" height="40" rx="2"/><path d="M30 14 H48 M30 22 H48 M30 30 H42"/><circle cx="16" cy="30" r="6"/><path d="M6 54 V46 Q16 38 26 46 V54"/></svg>
  <h3>SEAL THE DEAL</h3>
  <p>Work closely with your agent to buy or sell your home with confidence.</p>
</div>

<!-- WHY -->
<h2 class="abs sec-title" style="top:1675px"><span class="h-light">Why</span> <span class="h-bold" style="font-weight:600">HarborMatch?</span></h2>
<div class="abs" style="left:563px;top:1732px;width:74px;height:3px;background:var(--blue)"></div>
<p class="abs" style="left:0;top:1758px;width:1200px;text-align:center;font-size:19px;color:var(--navy)">Your one-stop shop for buying or selling a property</p>

<svg class="abs" style="left:350px;top:1795px" width="500" height="510"><circle cx="250" cy="255" r="235" fill="none" stroke="#c8dbef" stroke-width="2"/><g fill="#3b5d99"><circle cx="6" cy="170" r="4"/><circle cx="14" cy="340" r="4"/><circle cx="494" cy="175" r="4"/><circle cx="448" cy="348" r="4"/></g></svg>
<div class="abs" style="left:393px;top:1855px;width:400px;height:400px;border-radius:50%;border:3px solid #d4e4f3;background:#fff"></div>
<div class="abs" role="img" aria-label="Isometric modern two-storey house with glass walls" style="left:410px;top:1872px;width:366px;height:366px;border-radius:50%;background:radial-gradient(circle at 50% 40%,#dfe9f4,#b8cde2 70%,#a9bfd6)"></div>

<div class="abs feat right-al" style="left:62px;top:1860px"><h4>Expert Agents</h4><p>Work with top-rated agents who<br>specialize in your market.</p></div>
<div class="abs icon-c b" style="left:348px;top:1854px"><svg width="34" height="34" fill="none" stroke="#fff" stroke-width="2"><circle cx="12" cy="10" r="6"/><path d="M2 32 Q12 18 22 32"/><rect x="20" y="6" width="12" height="10" rx="2"/></svg></div>
<div class="abs feat right-al" style="left:24px;top:2012px"><h4>Personalized Matches</h4><p>Get connected with agents<br>tailored to your unique needs.</p></div>
<div class="abs icon-c n" style="left:308px;top:2015px"><svg width="34" height="34" fill="none" stroke="#fff" stroke-width="2"><rect x="6" y="4" width="20" height="26" rx="2"/><path d="M11 12 H21 M11 18 H21"/><circle cx="25" cy="25" r="6"/></svg></div>
<div class="abs feat right-al" style="left:90px;top:2190px"><h4>Fast Connections</h4><p>Quickly find the right agent and<br>get started immediately.</p></div>
<div class="abs icon-c b" style="left:372px;top:2180px"><svg width="34" height="34" fill="none" stroke="#fff" stroke-width="2"><circle cx="17" cy="10" r="6"/><path d="M4 32 Q17 16 30 32"/><path d="M2 22 H10 M24 22 H32"/></svg></div>

<div class="abs icon-c n" style="left:738px;top:1854px"><svg width="34" height="34" fill="none" stroke="#fff" stroke-width="2"><path d="M4 18 L17 6 L30 18 V30 H4 Z"/><circle cx="17" cy="20" r="5"/></svg></div>
<div class="abs feat" style="left:825px;top:1858px"><h4>Comprehensive Support</h4><p>Receive guidance and assistance<br>throughout your real estate journey</p></div>
<div class="abs icon-c b" style="left:784px;top:2015px"><svg width="34" height="34" fill="none" stroke="#fff" stroke-width="2"><circle cx="17" cy="17" r="5"/><circle cx="6" cy="6" r="3"/><circle cx="28" cy="6" r="3"/><circle cx="6" cy="28" r="3"/><circle cx="28" cy="28" r="3"/><path d="M9 9 L13 13 M25 9 L21 13 M9 25 L13 21 M25 25 L21 21"/></svg></div>
<div class="abs feat" style="left:869px;top:2018px"><h4>Exclusive Network</h4><p>Access a curated network of elite<br>real estate professionals.</p></div>
<div class="abs icon-c n" style="left:712px;top:2180px"><svg width="34" height="34" fill="none" stroke="#fff" stroke-width="2"><path d="M4 18 L17 6 L30 18 V30 H4 Z"/><path d="M12 20 L16 24 L23 16"/></svg></div>
<div class="abs feat" style="left:803px;top:2190px"><h4>Trusted Process</h4><p>Rely on our proven method for<br>successful agent-client matches.</p></div>

<span class="abs btn btn-orange" style="left:500px;top:2307px;width:190px;height:42px">Get Started Now</span>

<!-- TESTIMONIALS -->
<div class="fill" role="img" aria-label="Pale blue skyline silhouettes behind the testimonials" style="left:0;top:2440px;width:1200px;height:530px;background:linear-gradient(180deg,#fff 0%,#eef4fb 20%,#e8f0f9 70%,#dce8f4 92%,#fff 100%)"></div>
<h2 class="abs sec-title" style="top:2498px;font-size:38px"><span class="h-light" style="font-weight:400">What People</span> <span class="h-bold" style="font-weight:600">are Saying</span></h2>
<div class="abs tcard" style="left:112px"><span class="q">“</span>
  <p>HarborMatch matched me with Caleb, and I couldn’t be happier! Thanks to Caleb’s expertise, I got my very first home for $15K UNDER the highest offer in Lakewood. Idk how he did it but man did he make a difference.</p>
  <div class="who"><span class="avatar"></span><span>Marcus L.<span class="stars">★★★★★</span></span></div><span class="rev"></span></div>
<div class="abs tcard" style="left:448px"><span class="q">“</span>
  <p>I had an exceptional experience with HarborMatch. From the moment I was matched with my agent, everything just clicked. The entire process, from our first conversation to closing, was handled with the utmost professionalism.</p>
  <div class="who"><span class="avatar"></span><span>Nora &amp; Eli<span class="stars">★★★★★</span></span></div><span class="rev"></span></div>
<div class="abs tcard" style="left:786px"><span class="q">“</span>
  <p>HarborMatch connected me with an outstanding agent who knew the Denver market inside and out. Thanks to his expertise and guidance, I was able to sell my house for $20K over the asking price. I highly recommend HarborMatch for anyone looking to sell their home.</p>
  <div class="who"><span class="avatar"></span><span>Owen P.<span class="stars">★★★★★</span></span></div><span class="rev"></span></div>

<!-- SUCCESS STORY -->
<div class="abs story">
  <h2>Success <b>Stories</b></h2>
  <p>I had an exceptional experience with HarborMatch. From the moment I was matched with my agent, everything just clicked. The entire process, from our first conversation to closing, was handled with the utmost professionalism. I felt like I was in great hands the whole time, and I couldn’t be more satisfied with how things turned out.</p>
  <div class="name">Nora &amp; Eli</div>
  <svg class="abs" style="left:315px;top:393px" width="120" height="30" fill="none" stroke-width="2"><path d="M30 15 H2 M10 7 L2 15 L10 23" stroke="#8fbff0"/><path d="M62 15 H90 M82 7 L90 15 L82 23" stroke="#fff"/></svg>
  <svg class="abs" style="left:740px;top:365px" width="80" height="70"><path d="M6 60 Q2 20 34 6 L36 14 Q22 24 24 34 A14 14 0 1 1 6 60Z M46 60 Q42 20 74 6 L76 14 Q62 24 64 34 A14 14 0 1 1 46 60Z" fill="#fff"/></svg>
</div>
<svg class="abs" style="left:80px;top:3135px" width="390" height="390"><circle cx="195" cy="195" r="188" fill="none" stroke="#1a73d9" stroke-width="2" stroke-dasharray="6 5"/></svg>
<div class="abs" role="img" aria-label="Happy couple holding house keys and giving a thumbs up" style="left:90px;top:3145px;width:370px;height:370px;border-radius:50%;background:radial-gradient(circle at 50% 45%,#f2f4f7,#d7dde5 70%,#c4ccd7)"></div>

<!-- CONTACT FORM -->
<h2 class="abs sec-title" style="top:3650px;font-size:36px;line-height:42px;font-weight:400"><span class="h-light" style="font-weight:400">Find Your Best Realtor to</span><br><span class="h-bold" style="font-weight:600">Sell or Buy Home</span></h2>
<div class="abs" style="left:552px;top:3748px;width:66px;height:3px;background:var(--blue)"></div>
<div class="fill" role="img" aria-label="Blue city skyline with mountains and green parkland" style="left:0;top:3790px;width:1200px;height:300px;background:linear-gradient(180deg,#cfe3f5 0%,#7fb7e8 40%,#5d9fde 60%,#d8ec9a 85%,#f2f8e0 100%)"></div>
<div class="abs form-card">
  <div class="field" style="left:46px;top:48px;width:242px">First Name</div>
  <div class="field" style="left:298px;top:48px;width:245px">Last Name</div>
  <div class="field" style="left:553px;top:48px;width:245px">Email address</div>
  <div class="field" style="left:46px;top:110px;width:242px">Phone Number</div>
  <div class="field" style="left:298px;top:110px;width:245px">What you are looking for<svg width="12" height="8"><path d="M1 1 L6 6 L11 1" fill="none" stroke="#333" stroke-width="1.5"/></svg></div>
  <div class="field" style="left:553px;top:110px;width:245px">City<svg width="12" height="8"><path d="M1 1 L6 6 L11 1" fill="none" stroke="#333" stroke-width="1.5"/></svg></div>
  <div class="field" style="left:46px;top:172px;width:752px;height:96px">Additional Details</div>
  <span class="abs btn btn-orange" style="left:323px;top:315px;width:205px;height:46px;font-size:16px">Send Message</span>
</div>

<!-- FOOTER -->
<div class="abs brand" style="left:143px;top:4380px">HarborMatch</div>
<p class="abs" style="left:143px;top:4425px;width:270px;font-size:11px;line-height:15px;color:#555">Experience personalized service, unmatched expertise, and rapid connections with top agents tailored to your unique needs.</p>
<p class="abs" style="left:143px;top:4510px;font-size:10px;color:#666">© 2024 HarborMatch. All Rights Reserved</p>
<div class="abs vline" style="left:447px"></div>
<div class="abs vline" style="left:680px"></div>
<div class="abs vline" style="left:880px"></div>
<div class="abs footer-col" style="left:494px;top:4375px"><h5>Quick Links</h5><ul><li>Home</li><li>About Us</li><li>Features</li><li>How it works</li></ul></div>
<div class="abs footer-col" style="left:730px;top:4375px"><h5>Resources</h5><ul><li>Testimonials</li><li>Blogs</li><li>Why Us</li><li>Contact Us</li></ul></div>
<div class="abs footer-col" style="left:938px;top:4375px"><h5>Follow Us</h5></div>
<div class="abs" style="left:942px;top:4412px;display:flex;gap:6px"><span class="soc"></span><span class="soc"></span><span class="soc"></span><span class="soc"></span></div>

</body>
</html>
```